3 x Webpage Homepage Banner for New Scrap Metal Company website

New website (currently under construction) for a scrap metal recycling company require 3 home page banner that give visitor have a sense of confident and relevance in the company. Feeling good about the products and value.

I have attached here a file name "website home page" to show the currently general idea of the design of the webpage. Two more file "Regular Login 1" and "Regular Login 2" to show the currently "looks" when a user visit the page. The current banner is a dummy.

One of the file titled "Company Image" is the picture of our company which I would also like to have it in one of the banner.

```html
<!DOCTYPE html>
<html lang="en">
<head>
<meta charset="utf-8">
<title>Tan Keat Recycling – Homepage Banners</title>
<link href="https://fonts.googleapis.com/css2?family=Roboto:wght@300;400;500;700&display=swap" rel="stylesheet">
<style>
  :root{
    --stage:#f2cc74;
    --white:#ffffff;
    --gold:#c8902a;
    --gold-light:#e0ad48;
    --gold-dark:#b57f1f;
    --navy:#0b1a7c;
    --cart:#1b4a7a;
    --ink-soft:#9a9a9a;
    --line:#d9d9d9;
  }
  *{box-sizing:border-box;margin:0;padding:0}
  html,body{width:1108px;height:1200px;overflow:hidden}
  body{background:var(--stage);font-family:'Roboto',sans-serif;position:relative}

  .banner{position:absolute;left:115px;width:877px;height:347px;background:var(--white);
    box-shadow:14px 16px 18px rgba(120,80,10,.35)}
  .banner--one{top:42px}
  .banner--two{top:426px}
  .banner--three{top:809px}

  .site-header{position:relative;height:37px;background:var(--white)}
  .brand{position:absolute;left:202px;top:9px;display:flex;align-items:center;gap:6px}
  .brand__mark{width:22px;height:22px;border:2px solid var(--gold);border-radius:2px}
  .brand__name{font-size:9px;font-weight:500;color:var(--gold);letter-spacing:.6px;text-transform:uppercase;line-height:1}
  .search{position:absolute;left:411px;top:12px;width:145px;height:15px;border:1px solid var(--line);
    border-radius:8px;font-size:6px;color:var(--ink-soft);padding:3px 9px;display:flex;justify-content:space-between}
  .search svg{width:7px;height:7px}
  .cart{position:absolute;left:578px;top:0;width:95px;height:29px;background:var(--cart);border-radius:0 0 4px 4px;
    display:flex;align-items:center;gap:6px;padding-left:14px;color:var(--white)}
  .cart svg{width:15px;height:12px}
  .cart__title{font-size:6px;font-weight:700;line-height:8px}
  .cart__meta{font-size:5px;line-height:7px}

  .site-nav{position:relative;height:18px;background:linear-gradient(var(--gold-light),var(--gold-dark));
    display:flex;align-items:center;padding-left:203px;gap:16px}
  .site-nav a{font-size:5.5px;color:var(--white);text-decoration:none;font-weight:500;letter-spacing:.2px}
  .site-nav a.is-active{font-weight:700;border-bottom:1px solid var(--white);padding-bottom:1px}
  .login{position:absolute;left:641px;top:5px;font-size:5.5px;color:var(--white);display:flex;gap:5px;align-items:center}
  .login svg{width:6px;height:6px}

  .hero{position:relative;height:292px;overflow:hidden}
  .hero__photo{position:absolute;inset:0}
  .hero--facility .hero__photo{background:linear-gradient(100deg,var(--navy) 0%,var(--navy) 38%,#1f3fb3 55%,#e9ece4 70%,#2a49b8 85%,#1a2c86 100%)}
  .hero--yard .hero__photo{background:linear-gradient(100deg,#3a1f0a 0%,#7a4a1c 30%,#b46e2c 55%,#d79a56 75%,#8c5224 100%)}
  .hero--metal .hero__photo{background:radial-gradient(ellipse at 65% 45%,#a98e5c 0%,#6b5128 45%,#2e2010 100%)}
  .hero__rule{position:absolute;left:0;right:0;bottom:18px;height:2px;background:var(--gold)}

  .hero__copy{position:absolute;color:var(--white)}
  .hero--facility .hero__copy{left:105px;top:76px}
  .hero--yard .hero__copy{left:105px;top:74px}
  .hero__title{font-weight:400;font-size:28px;line-height:31px}
  .hero__lead{font-weight:300;font-size:15.5px;margin-top:8px}
  .hero--yard .hero__title{font-size:28px;letter-spacing:.5px}
  .hero--yard .hero__lead{font-size:20px;margin-top:0}
  .hero--metal .hero__copy{left:0;right:0;top:76px;text-align:center}
  .hero--metal .hero__title{font-weight:700;font-size:29px;letter-spacing:.3px}
  .hero--metal .hero__lead{font-size:18.5px;font-weight:300;line-height:31px;margin-top:4px}
</style>
</head>
<body>

<section class="banner banner--one">
  <header class="site-header">
    <div class="brand"><span class="brand__mark"></span><span class="brand__name">Tan Keat Recycling</span></div>
    <div class="search">Search<svg viewBox="0 0 10 10"><circle cx="4" cy="4" r="3" fill="none" stroke="#bbb"/><path d="M6.5 6.5 9 9" stroke="#bbb"/></svg></div>
    <div class="cart"><svg viewBox="0 0 16 12"><path d="M1 1h2l2 7h8l2-5H4" fill="none" stroke="#fff" stroke-width="1.2"/><circle cx="6" cy="10.5" r="1" fill="#fff"/><circle cx="12" cy="10.5" r="1" fill="#fff"/></svg>
      <div><div class="cart__title">MY CART</div><div class="cart__meta">0 items - SGD 0.00</div></div></div>
  </header>
  <nav class="site-nav"><a class="is-active">HOME</a><a>ABOUT US</a><a>PRODUCTS</a><a>OUR SERVICES</a><a>INVESTORS</a><a>CONTACT US</a>
    <span class="login"><svg viewBox="0 0 6 6"><circle cx="3" cy="1.6" r="1.4" fill="#fff"/><path d="M0 6a3 2.5 0 0 1 6 0z" fill="#fff"/></svg>LOG IN</span></nav>
  <div class="hero hero--facility">
    <div class="hero__photo" role="img" aria-label="Photo of the company's blue and white recycling facility building against a blue sky"></div>
    <div class="hero__copy"><h1 class="hero__title">Recycling<br>Industrial Metal Scraps</h1><p class="hero__lead">We are the leading industry scrap provider.</p></div>
    <div class="hero__rule"></div>
  </div>
</section>

<section class="banner banner--two">
  <header class="site-header">
    <div class="brand"><span class="brand__mark"></span><span class="brand__name">Tan Keat Recycling</span></div>
    <div class="search">Search<svg viewBox="0 0 10 10"><circle cx="4" cy="4" r="3" fill="none" stroke="#bbb"/><path d="M6.5 6.5 9 9" stroke="#bbb"/></svg></div>
    <div class="cart"><svg viewBox="0 0 16 12"><path d="M1 1h2l2 7h8l2-5H4" fill="none" stroke="#fff" stroke-width="1.2"/><circle cx="6" cy="10.5" r="1" fill="#fff"/><circle cx="12" cy="10.5" r="1" fill="#fff"/></svg>
      <div><div class="cart__title">MY CART</div><div class="cart__meta">0 items - SGD 0.00</div></div></div>
  </header>
  <nav class="site-nav"><a class="is-active">HOME</a><a>ABOUT US</a><a>PRODUCTS</a><a>OUR SERVICES</a><a>INVESTORS</a><a>CONTACT US</a>
    <span class="login"><svg viewBox="0 0 6 6"><circle cx="3" cy="1.6" r="1.4" fill="#fff"/><path d="M0 6a3 2.5 0 0 1 6 0z" fill="#fff"/></svg>LOG IN</span></nav>
  <div class="hero hero--yard">
    <div class="hero__photo" role="img" aria-label="Photo of compressed bales of scrap metal stacked in a scrap yard, warm copper tones"></div>
    <div class="hero__copy"><h1 class="hero__title">AUTHORIZED</h1><p class="hero__lead">Fully Equipped Scrap Yard</p></div>
    <div class="hero__rule"></div>
  </div>
</section>

<section class="banner banner--three">
  <header class="site-header">
    <div class="brand"><span class="brand__mark"></span><span class="brand__name">Tan Keat Recycling</span></div>
    <div class="search">Search<svg viewBox="0 0 10 10"><circle cx="4" cy="4" r="3" fill="none" stroke="#bbb"/><path d="M6.5 6.5 9 9" stroke="#bbb"/></svg></div>
    <div class="cart"><svg viewBox="0 0 16 12"><path d="M1 1h2l2 7h8l2-5H4" fill="none" stroke="#fff" stroke-width="1.2"/><circle cx="6" cy="10.5" r="1" fill="#fff"/><circle cx="12" cy="10.5" r="1" fill="#fff"/></svg>
      <div><div class="cart__title">MY CART</div><div class="cart__meta">0 items - SGD 0.00</div></div></div>
  </header>
  <nav class="site-nav"><a class="is-active">HOME</a><a>ABOUT US</a><a>PRODUCTS</a><a>OUR SERVICES</a><a>INVESTORS</a><a>CONTACT US</a>
    <span class="login"><svg viewBox="0 0 6 6"><circle cx="3" cy="1.6" r="1.4" fill="#fff"/><path d="M0 6a3 2.5 0 0 1 6 0z" fill="#fff"/></svg>LOG IN</span></nav>
  <div class="hero hero--metal">
    <div class="hero__photo" role="img" aria-label="Close-up photo of a pile of shredded metal pellets in silver and bronze"></div>
    <div class="hero__copy"><h1 class="hero__title">SCRAP METAL RECYCLING</h1><p class="hero__lead">Ferrous &nbsp;|&nbsp; Non-Ferrous &nbsp;|&nbsp; Machineries<br>Electronics &nbsp;|&nbsp; Industrial</p></div>
    <div class="hero__rule"></div>
  </div>
</section>

</body>
</html>
```